Build Distinctive Business Card: Public Relations Government Relations firm

I have logo and colors done (attached) need a very cool way to present it on a business card (can be two sided if need be).

Public Relations Government Relations firm

Info:

Mark Tillson, CEO
Keystone Public Relations
2786 West Harlow Blvd.
Los Angeles CA 90047
(o) 213.555.0148
(f) 213.555.0193
mark@keystonekpr-example.com

Target Market(s)

Government relations, public relations, lobbyist, I was a past State Senator

Industry/Entity Type

Business

Contact Information for Business Card

Info:

Mark Tillson, CEO
Keystone Public Relations
2786 West Harlow Blvd.
Los Angeles CA 90047
(o) 213.555.0148
(f) 213.555.0193
mark@keystonekpr-example.com
@marktillson

Requirements
Must have
• A sense of balance given logo is already done.
• It's a government relations firm really.
• Lobbyist type.
• Senatorial type...

```html
<!DOCTYPE html>
<html lang="en">
<head>
<meta charset="utf-8">
<title>Keystone Public Relations – Business Card</title>
<link href="https://fonts.googleapis.com/css2?family=Arimo:wght@400;700&display=swap" rel="stylesheet">
<style>
  :root {
    --backdrop: #003360;
    --card-front: #ffffff;
    --card-back: #000000;
    --brand-blue: #0a5aa8;
    --brand-blue-light: #1a78d2;
    --ink: #111111;
    --ink-light: #ffffff;
  }
  * { margin: 0; padding: 0; box-sizing: border-box; }
  html, body {
    width: 1200px;
    height: 1000px;
    overflow: hidden;
    background: var(--backdrop);
    font-family: "Arimo", Helvetica, Arial, sans-serif;
  }
  .stage { position: relative; width: 1200px; height: 1000px; }
  .card {
    position: absolute;
    top: 196px;
    width: 357px;
    height: 607px;
    border-radius: 14px;
  }
  .card--front { left: 220px; background: var(--card-front); color: var(--ink); }
  .card--back { left: 623px; background: var(--card-back); color: var(--ink-light); }

  .brand {
    position: absolute;
    left: 28px;
    top: 53px;
    display: flex;
    align-items: center;
    gap: 12px;
  }
  .brand__dot {
    width: 108px;
    height: 108px;
    border-radius: 50%;
    background: var(--brand-blue);
    flex: none;
  }
  .brand__name {
    color: var(--brand-blue);
    font-weight: 700;
    line-height: 1;
  }
  .brand__name-main { display: block; font-size: 38px; letter-spacing: -0.5px; }
  .brand__name-sub {
    display: block;
    margin-top: 6px;
    font-size: 10px;
    letter-spacing: 2px;
    text-transform: uppercase;
    text-align: right;
  }

  .person {
    position: absolute;
    top: 283px;
    width: 100%;
    text-align: center;
  }
  .person__name { font-size: 20px; font-weight: 400; line-height: 1.2; }
  .person__name strong { font-weight: 700; }
  .person__title { font-size: 15px; line-height: 1.3; }

  .contact {
    position: absolute;
    top: 440px;
    width: 100%;
    text-align: center;
    font-size: 15px;
    line-height: 20px;
  }
  .contact__group + .contact__group { margin-top: 20px; }

  .back__mark {
    position: absolute;
    left: 89px;
    top: 349px;
    width: 178px;
    height: 178px;
    border-radius: 50%;
    background: var(--brand-blue-light);
  }
  .back__web {
    position: absolute;
    top: 561px;
    width: 100%;
    text-align: center;
    font-size: 18px;
    font-weight: 700;
  }
</style>
</head>
<body>
<main class="stage">
  <section class="card card--front">
    <div class="brand">
      <span class="brand__dot"></span>
      <span class="brand__name">
        <span class="brand__name-main">Keystone</span>
        <span class="brand__name-sub">Public Relations</span>
      </span>
    </div>
    <div class="person">
      <p class="person__name">Mark <strong>Tillson</strong></p>
      <p class="person__title">CEO</p>
    </div>
    <div class="contact">
      <div class="contact__group">
        <p>2786 West Harlow Blvd.</p>
        <p>Los Angeles CA 90047</p>
      </div>
      <div class="contact__group">
        <p>T:&nbsp; 213.555.0148</p>
        <p>F:&nbsp; 213.555.0193</p>
      </div>
      <div class="contact__group">
        <p>E:&nbsp; mark@keystonekpr-example.com</p>
      </div>
    </div>
  </section>

  <section class="card card--back">
    <span class="back__mark"></span>
    <p class="back__web">www.keystonekpr-example.com</p>
  </section>
</main>
</body>
</html>
```